Business card - Harbourline Stoneworks

Design a business card utilizing the given logo.
colors we like: Black, greys, Teal, blues.
Tri color card, horizontal orientation likely
Logo and name likely best on top.
Info on card:

Dennis Farrowby
#5 - 4180 Maple Ridge Blvd.
Surrey, B.C. V3K 2R9

778.555.0193
dennisfarrowby@brellnet.ca

Slogan: "Building Dreams"

We are a construction company that specializes in new home construction on the West coast of BC Canada. Open Concepts designs of high end homes.

```html
<!DOCTYPE html>
<html lang="en">
<head>
<meta charset="utf-8">
<title>Harbourline Stoneworks – Business Card</title>
<link rel="stylesheet" href="https://fonts.googleapis.com/css2?family=Abel&family=Michroma&display=swap">
<style>
  :root {
    --ink: #0a0a0a;
    --teal: #10b8a0;
    --paper: #ffffff;
    --ghost: #ebebeb;
    --backdrop-light: #8a8a8a;
    --backdrop-dark: #666666;
    --text: #1a1a1a;
  }
  * { box-sizing: border-box; margin: 0; padding: 0; }
  html, body {
    width: 1200px; height: 1000px; overflow: hidden;
  }
  body {
    background: radial-gradient(ellipse at 60% 70%, var(--backdrop-light), var(--backdrop-dark));
    position: relative;
  }
  .card {
    position: absolute;
    left: 100px; top: 191px;
    width: 1000px; height: 618px;
    overflow: hidden;
    background: var(--ink);
    box-shadow: 0 4px 14px rgba(0,0,0,0.35);
  }
  .card__shapes {
    position: absolute; inset: 0;
    width: 100%; height: 100%;
  }
  .brand {
    position: absolute;
    right: 114px; top: 70px;
    display: flex; align-items: center; gap: 34px;
  }
  .brand__dot {
    width: 130px; height: 130px;
    border-radius: 50%;
    background: var(--ink);
  }
  .brand__name {
    font-family: "Michroma", sans-serif;
    font-size: 42px;
    line-height: 1.2;
    color: var(--ink);
    text-align: right;
    letter-spacing: 1px;
  }
  .person {
    position: absolute;
    right: 114px; top: 262px;
    text-align: right;
  }
  .person__name {
    font-family: "Michroma", sans-serif;
    font-size: 30px;
    color: var(--teal);
    letter-spacing: 1px;
  }
  .person__title {
    font-family: "Abel", sans-serif;
    font-size: 24px;
    color: var(--text);
    margin-top: 4px;
  }
  .contact {
    position: absolute;
    left: 331px; top: 452px;
    list-style: none;
    font-family: "Abel", sans-serif;
    font-size: 25px;
    color: var(--text);
  }
  .contact__item {
    display: flex; align-items: center; gap: 12px;
    height: 30px;
  }
  .contact__icon {
    width: 21px; height: 21px; flex: none;
  }
</style>
</head>
<body>
  <article class="card">
    <svg class="card__shapes" viewBox="0 0 555 343" preserveAspectRatio="none" aria-hidden="true">
      <path d="M20,0 H555 V343 H228 C90,322 8,205 20,0 Z" fill="var(--teal)"/>
      <path d="M48,0 H555 V343 H252 C112,322 34,205 48,0 Z" fill="var(--paper)"/>
      <circle cx="470" cy="272" r="90" fill="var(--ghost)"/>
    </svg>

    <header class="brand">
      <span class="brand__dot"></span>
      <h1 class="brand__name">HARBOURLINE<br>STONEWORKS</h1>
    </header>

    <section class="person">
      <h2 class="person__name">Dennis Farrowby</h2>
      <p class="person__title">Managing Director</p>
    </section>

    <ul class="contact">
      <li class="contact__item">
        <svg class="contact__icon" viewBox="0 0 20 20" aria-hidden="true">
          <rect width="20" height="20" rx="4" fill="var(--teal)"/>
          <path d="M7 4 L9 7 L7.8 8.6 C8.6 10.4 9.8 11.6 11.4 12.3 L13 11 L16 13 L14.6 15.6 C9 15 5 11 4.4 5.4 Z" fill="#fff"/>
        </svg>
        778.555.0193
      </li>
      <li class="contact__item">
        <svg class="contact__icon" viewBox="0 0 20 20" aria-hidden="true">
          <rect width="20" height="20" rx="4" fill="var(--teal)"/>
          <rect x="4" y="6" width="12" height="8" fill="#fff"/>
          <path d="M4 6 L10 11 L16 6" stroke="var(--teal)" stroke-width="1.4" fill="none"/>
        </svg>
        dennisfarrowby@brellnet.ca
      </li>
      <li class="contact__item">
        <svg class="contact__icon" viewBox="0 0 20 20" aria-hidden="true">
          <rect width="20" height="20" rx="4" fill="var(--teal)"/>
          <path d="M10 3.5 C7.2 3.5 5.5 5.5 5.5 8 C5.5 11 10 16.5 10 16.5 C10 16.5 14.5 11 14.5 8 C14.5 5.5 12.8 3.5 10 3.5 Z" fill="#fff"/>
          <circle cx="10" cy="8" r="1.8" fill="var(--teal)"/>
        </svg>
        #5 - 4180 Maple Ridge Blvd. Surrey, B.C. V3K 2R9
      </li>
    </ul>
  </article>
</body>
</html>
```